Gourmet food made with love and care in my country kitchen

I'd like a business card designed for my small home-based food business. I have made labelling in federation blue for my food products (Labneh cheese, spicy pumpkin chutney, dukkah, caramelised onion jam, yo-Yo biscuits, chocolate mud cake etc) and have navy and white checked surrounds/borders on my brochures so would like to stick to these country colours.
Target Market(s)
Foodies who love gourmet delicacies. Everyone who enjoys a picnic that they don't have to prepare themselves.
Industry/Entity Type
Business
Contact Information for Business Card
Larkhollow Pantry
42 Tindale's Lane
Brimsworth Qld 4829
Phone Viv 07 48216597 or 0412386951
- Harrington

```html
<!DOCTYPE html>
<html lang="en">
<head>
<meta charset="utf-8">
<title>Larkhollow Pantry – Business Card</title>
<link rel="stylesheet" href="https://fonts.googleapis.com/css2?family=Pathway+Gothic+One&family=Kalam:wght@300&family=Libre+Baskerville:wght@400;700&display=swap">
<style>
  :root {
    --federation-blue: #8fb0dc;
    --navy: #3b4f9c;
    --ink: #1f1f24;
    --pattern-sky: #93b9e4;
    --paper: #ffffff;
    --text-grey: #3a3a3a;
  }
  * { margin: 0; padding: 0; box-sizing: border-box; }
  html, body {
    width: 1200px; height: 745px; overflow: hidden;
    background: var(--paper);
  }
  .card {
    position: relative; width: 1200px; height: 745px;
    background: var(--paper); font-family: "Libre Baskerville", Georgia, serif;
  }
  .panel-intro {
    position: absolute; left: 3px; top: 3px; width: 782px; height: 545px;
    background: var(--federation-blue);
    border: 3px solid var(--navy);
  }
  .panel-gallery {
    position: absolute; left: 782px; top: 3px; width: 415px; height: 545px;
    background: radial-gradient(circle at 30% 60%, #a9c8ec 0%, var(--pattern-sky) 55%, #7fa7d6 100%);
    border: 3px solid var(--navy);
  }
  .business-name {
    position: absolute; left: 0; top: 18px; width: 782px; text-align: center;
    font-family: "Pathway Gothic One", "Arial Narrow", sans-serif;
    font-size: 88px; line-height: 1; color: var(--ink);
  }
  .tagline {
    position: absolute; left: 22px; top: 130px; width: 760px;
    font-family: "Kalam", cursive; font-weight: 300;
    font-size: 29px; line-height: 48px; color: var(--ink);
  }
  .tagline .second-line { display: block; padding-left: 40px; }
  .services {
    position: absolute; left: 52px; top: 285px; list-style: none;
  }
  .services li {
    font-weight: 700; font-size: 39px; line-height: 81px; color: var(--ink);
  }
  .services li::before { content: ". "; }
  .photo {
    position: absolute; border: 3px solid #fff;
  }
  .photo-farm {
    left: 810px; top: 25px; width: 371px; height: 241px; border: none;
    background: linear-gradient(180deg, #cfe3f2 0%, #a9c9e2 32%, #6d8f55 45%, #4f7a32 70%, #5f8a3c 100%);
  }
  .photo-platter {
    left: 807px; top: 299px; width: 178px; height: 132px;
    transform: rotate(-12deg);
    background: linear-gradient(135deg, #d9cfc4 0%, #c98f5a 45%, #b8332a 70%, #e6ddd3 100%);
  }
  .photo-tart {
    left: 1006px; top: 310px; width: 155px; height: 195px;
    transform: rotate(8deg);
    background: linear-gradient(180deg, #dfe7e4 0%, #5b4a3c 35%, #d8a45c 60%, #2a2a2a 100%);
  }
  .contact {
    position: absolute; left: 0; width: 1200px; text-align: center; color: var(--text-grey);
  }
  .contact-address {
    top: 571px; font-variant: small-caps; font-weight: 700;
    font-size: 23px; letter-spacing: 1.5px;
  }
  .contact-phone { top: 615px; font-size: 27px; }
  .contact-email { top: 657px; font-size: 27px; }
  .contact-social { top: 698px; font-size: 27px; }
</style>
</head>
<body>
<main class="card">
  <section class="panel-intro">
    <h1 class="business-name">Larkhollow Pantry</h1>
    <p class="tagline">Gourmet food made in my country kitchen, using fresh
      <span class="second-line">ingredients, for your enjoyment and convenience. Viv Marsh</span></p>
    <ul class="services">
      <li>Gourmet Market Food</li>
      <li>Vintage Picnic Hampers</li>
      <li>Cooking Classes</li>
    </ul>
  </section>
  <section class="panel-gallery" role="img" aria-label="Soft blue and green bubble pattern background"></section>
  <div class="photo photo-farm" role="img" aria-label="Photo of a country paddock with gum trees, a white post fence and cane fields"></div>
  <div class="photo photo-platter" role="img" aria-label="Photo of a party platter of small tartlets and pastries"></div>
  <div class="photo photo-tart" role="img" aria-label="Photo of a rustic tart in a dark dish beside a bottle of wine on a verandah table"></div>

  <p class="contact contact-address">Kitchen 42 Tindale's Lane Brimsworth Qld 4829</p>
  <p class="contact contact-phone">Phone Viv: 07 48216597 or 0412386951</p>
  <p class="contact contact-email">Email: larkhollowpantry@postmail.com</p>
  <p class="contact contact-social">Socialpage: Larkhollow Pantry</p>
</main>
</body>
</html>
```